TovaLamarpe - Israeli Mental Health Website

We are developing an Israeli website for mental health. The website will be both in English and in Hebrew. We have a logo and would like a website design based on the logo and the logos colors (attached).

Attached is a doc that contains the website requirements.

We would like to have an icon for each of the sidebar categories, an image for each of the pages (including each of the sidebar category pages).

Target Market(s)

Adults 18-80

Industry/Entity Type

Mental Health

Number of Pages Required

5+ page

Font styles to use
Sans Serif

Colors

Designer to choose colors to be used in the design.

```html
<!DOCTYPE html>
<html lang="en">
<head>
<meta charset="utf-8">
<title>TovaLamarpe – Mental Health</title>
<link href="https://fonts.googleapis.com/css2?family=Poppins:wght@400;500;600;700&display=swap" rel="stylesheet">
<style>
:root{
  --blue:#2a78bd;
  --blue-dark:#1f5fa8;
  --green:#4caf48;
  --green-dark:#3e9a3e;
  --text:#333;
  --muted:#555;
  --grey-bg:#f1f1f1;
  --white:#fff;
}
*{box-sizing:border-box;margin:0;padding:0}
html,body{width:1200px;height:4196px;overflow:hidden;background:var(--white)}
body{font-family:"Poppins",sans-serif;color:var(--text);position:relative}
.abs{position:absolute}
a{color:inherit;text-decoration:none}

/* hero */
.hero{left:0;top:0;width:1200px;height:703px;background:linear-gradient(100deg,#f4f6f4 0%,#e7ece6 40%,#dfe5e8 70%,#eef1f3 100%)}
.hero-photo{left:380px;top:130px;width:820px;height:573px;background:radial-gradient(ellipse at 50% 45%,#c8cfc4 0%,#d6dcd8 40%,rgba(230,235,236,0) 75%)}
.sidebar{left:18px;top:24px;width:300px;height:652px;border-radius:10px;background:linear-gradient(180deg,var(--blue) 0%,#3a9a7a 55%,var(--green) 100%);padding:16px 12px}
.sidebar ul{list-style:none}
.sidebar li{display:flex;align-items:center;gap:18px;color:var(--white);font-size:16.5px;line-height:20px;min-height:43.5px;padding:0 14px}
.sidebar li.active{background:rgba(255,255,255,.12);border-radius:5px}
.sidebar li.tall{min-height:60px}
.sidebar svg{flex:none}
.brand{left:350px;top:22px;width:150px;text-align:center}
.brand-mark{display:block;width:40px;height:40px;margin:0 auto 4px;border-radius:50%;background:var(--green)}
.brand-name{font-size:22px;font-weight:600;color:var(--blue)}
.nav{left:545px;top:86px;display:flex;gap:44px;font-size:12px;font-weight:600;color:#222}
.lang{left:893px;top:20px;display:flex;align-items:center;gap:10px;font-size:22px;font-weight:600;color:#222}
.globe{width:34px;height:34px;border-radius:50%;background:var(--green-dark)}
.chat-top{left:1103px;top:18px;width:46px;height:46px;border-radius:50%;background:var(--green);border:3px solid var(--white);box-shadow:0 0 4px rgba(0,0,0,.2)}
.hero-title{left:375px;top:548px;font-size:66px;font-weight:700;color:var(--blue)}

/* shared */
h2{font-size:38px;font-weight:600;color:#333}
.copy{font-size:16.5px;line-height:25.5px;color:#444}
.btn{display:flex;align-items:center;justify-content:center;color:var(--white);font-weight:600;border-radius:32px;background:linear-gradient(180deg,var(--blue) 0%,var(--green) 100%);font-size:15px}
.photo{background:linear-gradient(135deg,#c9d3dc,#8e9fb0)}

/* emergency */
.em-ring{left:98px;top:822px;width:384px;height:374px;border-radius:50%;border-left:6px solid var(--green);border-bottom:6px solid var(--green)}
.em-photo{left:106px;top:824px;width:374px;height:370px;border-radius:50%;background:linear-gradient(135deg,#e7ece9,#6c8aa8 60%,#2c4b6a)}
.em-deco{left:720px;top:780px;width:430px;height:430px;border-radius:50%;border:30px solid rgba(76,175,72,.06)}
.em-title{left:521px;top:848px}
.em-copy{left:527px;top:906px;width:535px}
.em-btn{left:518px;top:1133px;width:392px;height:60px;font-weight:500}

/* chat band */
.chat-band{left:0;top:1341px;width:1200px;height:446px;background:var(--green)}
.chat-icon{left:540px;top:1302px;width:119px;height:119px;border-radius:50%;background:var(--green);border:5px solid var(--white);display:flex;align-items:center;justify-content:center}
.chat-title{left:0;top:1430px;width:1200px;text-align:center;color:var(--white)}
.chat-copy{left:230px;top:1492px;width:740px;text-align:center;color:var(--white);font-size:16.5px;line-height:25.5px}
.chat-btn{left:454px;top:1628px;width:290px;height:65px;border:4px solid var(--white);border-radius:34px;background:var(--blue-dark);color:var(--white);font-size:23px;font-weight:600;display:flex;align-items:center;justify-content:center}

/* therapists */
.ther-band{left:0;top:1787px;width:1200px;height:624px;background:var(--blue)}
.ther-title{left:153px;top:1918px;color:var(--white)}
.ther-copy{left:158px;top:1979px;width:525px;color:var(--white)}
.ther-btn{left:153px;top:2208px;width:204px;height:66px;border:4px solid var(--white);background:var(--green-dark)}
.ther-ring{left:708px;top:1898px;width:382px;height:374px;border-radius:50%;border-left:7px solid var(--green);border-top:7px solid var(--green)}
.ther-photo{left:724px;top:1900px;width:368px;height:368px;border-radius:50%;background:linear-gradient(135deg,#eef0ee,#c6c0b6 55%,#9a8b7d)}

/* organizations */
.org-square{left:101px;top:2540px;width:133px;height:138px;background:var(--green)}
.org-photo{left:135px;top:2572px;width:415px;height:412px;background:linear-gradient(135deg,#d9c9b6,#9a7f66 55%,#5a4a3f)}
.org-title{left:615px;top:2590px}
.org-copy{left:620px;top:2660px;width:495px}
.org-btn{left:617px;top:2890px;width:246px;height:57px}

/* videos */
.vid-box{left:52px;top:3093px;width:682px;height:559px;background:var(--grey-bg)}
.vid-title{left:130px;top:3212px}
.vid-copy{left:135px;top:3285px;width:300px}
.vid-btn{left:132px;top:3512px;width:185px;height:58px}
.vid-photo{left:464px;top:3171px;width:628px;height:391px;background:linear-gradient(120deg,#cfd7e0,#8ea3bd 55%,#4e6a90)}
.play{left:788px;top:3318px;width:106px;height:106px;border-radius:50%;background:#111;border:5px solid var(--white);display:flex;align-items:center;justify-content:center}

/* footer */
.foot-deco{left:780px;top:3900px;width:420px;height:300px;border-radius:50%;border:28px solid rgba(42,120,189,.05)}
.foot-brand{left:114px;top:3838px;width:317px;text-align:center}
.foot-brand .brand-mark{width:96px;height:96px;margin-bottom:16px}
.foot-brand .brand-name{font-size:46px}
.foot-col{top:3842px}
.foot-col h4{font-size:15.5px;font-weight:600;color:#333;margin-bottom:14px}
.foot-col .rule{display:flex;align-items:center;width:110px;height:2px;background:var(--blue);margin-bottom:30px}
.foot-col .rule::before{content:"";width:9px;height:9px;background:var(--green)}
.foot-col ul{list-style:none;font-size:13.5px;line-height:24px;color:#555;padding-left:6px}
.foot-col p{font-size:13.5px;line-height:19px;color:#555;width:190px}
.socials{display:flex;gap:12px;margin-top:18px}
.socials span{width:22px;height:22px;border-radius:50%;background:var(--blue)}
.foot-bottom{left:121px;top:4112px;width:925px;display:flex;justify-content:space-between;font-size:14.5px;color:#333}
.foot-bottom nav{display:flex;gap:78px}
.foot-bottom nav a{text-decoration:underline}
</style>
</head>
<body>

<!-- Hero -->
<section class="abs hero"></section>
<div class="abs hero-photo" role="img" aria-label="Blended portrait of a calm woman and a distressed woman"></div>

<aside class="abs sidebar">
  <ul>
    <li class="active"><svg width="22" height="22" viewBox="0 0 24 24" fill="none" stroke="#fff" stroke-width="2"><path d="M5 3h4l2 5-3 2a11 11 0 0 0 6 6l2-3 5 2v4a2 2 0 0 1-2 2A17 17 0 0 1 3 5a2 2 0 0 1 2-2z"/></svg>Emergency Mental Help</li>
    <li><svg width="22" height="22" viewBox="0 0 24 24" fill="none" stroke="#fff" stroke-width="2"><circle cx="12" cy="5" r="2"/><path d="M12 8v13M8 12h8"/></svg>Suicide</li>
    <li class="tall"><svg width="22" height="22" viewBox="0 0 24 24" fill="none" stroke="#fff" stroke-width="2"><circle cx="12" cy="12" r="8"/><path d="M8 8l8 8"/></svg>Sexual Assault/<br>Violence Victims</li>
    <li class="tall"><svg width="22" height="22" viewBox="0 0 24 24" fill="none" stroke="#fff" stroke-width="2"><path d="M3 12h14l4-4M17 12l4 4"/></svg>Sexual Assault/<br>Violence Assaulters</li>
    <li><svg width="22" height="22" viewBox="0 0 24 24" fill="none" stroke="#fff" stroke-width="2"><circle cx="12" cy="6" r="3"/><path d="M6 21l3-9h6l3 9"/></svg>Post Trauma</li>
    <li><svg width="22" height="22" viewBox="0 0 24 24" fill="#fff"><circle cx="12" cy="8" r="5"/><path d="M4 22c0-6 4-9 8-9s8 3 8 9z"/></svg>Depression</li>
    <li><svg width="22" height="22" viewBox="0 0 24 24" fill="#fff"><circle cx="12" cy="12" r="9"/></svg>Anxiety</li>
    <li><svg width="22" height="22" viewBox="0 0 24 24" fill="none" stroke="#fff" stroke-width="2"><rect x="9" y="3" width="6" height="18" rx="2"/><path d="M3 21h18"/></svg>Addictions</li>
    <li><svg width="22" height="22" viewBox="0 0 24 24" fill="none" stroke="#fff" stroke-width="2"><rect x="4" y="4" width="16" height="16" rx="2"/><path d="M8 14h8"/></svg>Sleep Disorders</li>
    <li><svg width="22" height="22" viewBox="0 0 24 24" fill="none" stroke="#fff" stroke-width="2"><path d="M7 3v18M4 3v6h6V3M17 3v18"/></svg>Eating Disorders</li>
    <li><svg width="22" height="22" viewBox="0 0 24 24" fill="none" stroke="#fff" stroke-width="2"><circle cx="12" cy="8" r="4"/><path d="M4 20h16"/></svg>Financial Problems</li>
    <li><svg width="22" height="22" viewBox="0 0 24 24" fill="#fff"><circle cx="7" cy="6" r="3"/><circle cx="17" cy="6" r="3"/><rect x="4" y="11" width="6" height="10"/><rect x="14" y="11" width="6" height="10"/></svg>Parenthood</li>
    <li><svg width="22" height="22" viewBox="0 0 24 24" fill="none" stroke="#fff" stroke-width="2"><path d="M2 12l5-5 5 5 5-5 5 5-10 7z"/></svg>Relationship</li>
  </ul>
</aside>

<div class="abs brand"><span class="brand-mark"></span><span class="brand-name">TovaLamarpe</span></div>
<nav class="abs nav"><a>THERAPISTS</a><a>ORGANIZATIONS</a><a>VIDEOS</a><a>CONTACT</a><a>ABOUT</a><a>DONATE</a></nav>
<div class="abs lang"><span class="globe"></span>English ▾</div>
<div class="abs chat-top"></div>
<div class="abs hero-title">TovaLamarpe</div>

<!-- Emergency -->
<div class="abs em-deco"></div>
<div class="abs em-ring"></div>
<div class="abs em-photo" role="img" aria-label="Man holding his head in distress"></div>
<h2 class="abs em-title">Emergency Mental Help</h2>
<p class="abs copy em-copy">Lorem ipsum dolor sit amet, consectetur adipiscing elit, sed do eiusmod tempor incididunt ut labore et dolore magna aliqua. Ut enim ad minim veniam, quis nostrud exercitation ullamco laboris nisi ut aliquip ex ea commodo consequat. Duis aute irure dolor in reprehenderit in voluptate velit esse cillum dolore eu fugiat nulla pariatur. Excepteur sint occaecat cupidatat non proident, sunt in culpa qui officia deserunt mollit anim id est laborum.</p>
<a class="abs btn em-btn">More options for Emergency Mental Help</a>

<!-- Chat band -->
<section class="abs chat-band"></section>
<div class="abs chat-icon"><svg width="52" height="52" viewBox="0 0 24 24" fill="none" stroke="#fff" stroke-width="2"><path d="M5 3h4l2 5-3 2a11 11 0 0 0 6 6l2-3 5 2v4a2 2 0 0 1-2 2A17 17 0 0 1 3 5a2 2 0 0 1 2-2z"/></svg></div>
<h2 class="abs chat-title" style="color:#fff">Smart ChatLine</h2>
<p class="abs chat-copy">Lorem ipsum dolor sit amet, consectetur adipiscing elit, sed do eiusmod tempor incididunt ut labore et dolore magna aliqua. Ut enim ad minim veniam, quis nostrud exercitation ullamco laboris nisi ut aliquip ex ea commodo consequat. Duis aute irure dolor in reprehenderit in voluptate velit esse cillum dolore eu fugiat</p>
<a class="abs chat-btn">XXXX5 123 X456</a>

<!-- Therapists -->
<section class="abs ther-band"></section>
<h2 class="abs ther-title" style="color:#fff">Therapists</h2>
<p class="abs copy ther-copy" style="color:#fff">Lorem ipsum dolor sit amet, consectetur adipiscing elit, sed do eiusmod tempor incididunt ut labore et dolore magna aliqua. Ut enim ad minim veniam, quis nostrud exercitation ullamco laboris nisi ut aliquip ex ea commodo consequat. Duis aute irure dolor in reprehenderit in voluptate velit esse cillum dolore eu fugiat nulla pariatur. Excepteur sint occaecat cupidatat non proident, sunt in culpa qui officia deserunt mollit anim id est laborum.</p>
<a class="abs btn ther-btn">FIND THERAPISTS</a>
<div class="abs ther-ring"></div>
<div class="abs ther-photo" role="img" aria-label="Therapist talking with a client on a sofa"></div>

<!-- Organizations -->
<div class="abs org-square"></div>
<div class="abs org-photo" role="img" aria-label="Two women embracing in a support group"></div>
<h2 class="abs org-title">Organizations</h2>
<p class="abs copy org-copy">Lorem ipsum dolor sit amet, consectetur adipiscing elit, sed do eiusmod tempor incididunt ut labore et dolore magna aliqua. Ut enim ad minim veniam, quis nostrud exercitation ullamco laboris nisi ut aliquip ex ea commodo consequat. Duis aute irure dolor in reprehenderit in voluptate velit esse cillum dolore eu fugiat nulla pariatur. Excepteur sint occaecat cupidatat non proident, sunt in culpa qui officia deserunt mollit anim id est laborum.</p>
<a class="abs btn org-btn">FIND ORGANIZATIONS</a>

<!-- Videos -->
<div class="abs vid-box"></div>
<h2 class="abs vid-title">Videos</h2>
<p class="abs copy vid-copy">Lorem ipsum dolor sit amet, cons ectetur adipiscing elit, sed do eius mod tempor incididunt ut labore et dolore magna aliqua. Ut enim ad minim veniam, quis nostrud exer citation ullamco laboris nisi ualiqu ip ex ea commodo consequat.</p>
<a class="abs btn vid-btn">VIDEO LIBRARY</a>
<div class="abs vid-photo" role="img" aria-label="Counselling session with a young man"></div>
<div class="abs play"><svg width="44" height="44" viewBox="0 0 24 24"><path d="M7 4l14 8-14 8z" fill="#fff"/></svg></div>

<!-- Footer -->
<div class="abs foot-deco"></div>
<div class="abs foot-brand"><span class="brand-mark"></span><span class="brand-name">TovaLamarpe</span></div>
<div class="abs foot-col" style="left:495px">
  <h4>QUICK LINKS</h4><div class="rule"></div>
  <ul><li>Home</li><li>About Us</li><li>Services</li><li>News</li><li>Contact</li></ul>
</div>
<div class="abs foot-col" style="left:682px">
  <h4>SUPPORT</h4><div class="rule"></div>
  <ul><li>Support</li><li>Help</li><li>Privacy Policy</li><li>Terms and Conditions</li></ul>
</div>
<div class="abs foot-col" style="left:877px">
  <h4>CONNECT ME</h4><div class="rule"></div>
  <p>Lorem ipsum dolor sit amet ons ectetur adipiscieliuis</p>
  <div class="socials"><span></span><span></span><span></span></div>
</div>
<div class="abs foot-bottom">
  <span>TovaLamarpe - Organization for Mental Health ©2023</span>
  <nav><a>Privacy Policy</a><a>Terms</a></nav>
</div>

</body>
</html>
```